Corporate Design für spanische Bauträgerfirma
Zielgruppe
Wir sind eine spanische Bauträgerfirma. Spezialisiert auf die Region Palma de Mallorca. Deutscher Hintergrund. Das Design unserer Objekte ist im Außenbereich provencalisch angehaucht, im Interior warm-puristisch. Wir arbeiten immer mit sehr wenigen Materialien, bauen sehr hochwertig, versuchen die Kubatur und Formensprache der Umgebung zu implementieren, dabei im Interior reduziert mit edlen Materialien dem Käufer Raum für Akzentuierungen zu lassen. Im Anhang ein paar Renderings unseres neuesten Projekts und ein paar Bilder eines gebauten Hauses vor Endfertigstellung in erster Meereslinie in Portixol.
Aufgabenstellung
Kestrim heisst im spanischen ebenfalls Raubtier. Gemeint war es ein Bisschen als Ironie, daher sollte das Logo keinesfalls zu hart oder zu agressiv wirken ... Das Ganze kommt von rechnerkiste-shop.de, dort gibt es die Funkelsprudel, ein Energy Drink, der als Job Hobby einiger Mitarbeiter entstand und ein 'süsses' Raubtier darstellt. Bild von Dose siehe unten. Gerne kann das Logo sich an diesem 'Raubtier' auch anlehnen, muss aber überhaupt nicht!

```html
<!DOCTYPE html>
<html lang="de">
<head>
<meta charset="utf-8">
<title>Kestrim SL – Corporate Design</title>
<link rel="stylesheet" href="https://fonts.googleapis.com/css2?family=Open+Sans:wght@400;600&display=swap">
<style>
:root{
  --orange:#f26a1b;
  --navy:#1e2a38;
  --ink:#2a3442;
  --stone:#9a9896;
  --paper:#ffffff;
  --mist:#f2f2f2;
  --body:#4a4f57;
  --faint:#e9e9eb;
}
*{margin:0;padding:0;box-sizing:border-box}
html,body{width:1200px;height:632px;overflow:hidden}
body{background:var(--mist);font-family:"Open Sans",Arial,sans-serif;color:var(--ink);position:relative}
.band{position:absolute;left:0;width:1200px}
.band--light{top:27px;height:240px;background:var(--paper)}
.band--dark{top:267px;height:248px;background:var(--navy)}
.tile{position:absolute;top:515px;height:93px;display:flex;align-items:center;justify-content:center;gap:7px}
.tile--stone{left:0;width:151px;background:var(--stone)}
.tile--white{left:151px;width:159px;background:var(--paper)}

.brand{position:absolute;display:flex;flex-direction:column;align-items:center}
.brand__dot{border-radius:50%;background:var(--orange)}
.brand__name{font-weight:400;white-space:nowrap;letter-spacing:.12em}
.brand--hero{left:25px;width:260px}
.brand--hero .brand__dot{width:46px;height:46px;margin-bottom:22px}
.brand--hero .brand__name{font-size:28px}
.brand--top{top:100px}
.brand--top .brand__name{color:var(--ink)}
.brand--mid{top:338px}
.brand--mid .brand__name{color:#fff}
.tile .brand__dot{width:10px;height:10px;border-radius:50%}
.tile .brand__name{font-size:12px;letter-spacing:.1em}
.tile--stone .brand__dot{background:#fff}
.tile--stone .brand__name{color:#fff}
.tile--white .brand__dot{background:var(--stone)}
.tile--white .brand__name{color:var(--stone)}

.letterhead{position:absolute;left:311px;top:41px;width:388px;height:546px;background:var(--paper);box-shadow:0 2px 8px rgba(0,0,0,.18)}
.letterhead .brand{right:38px;top:32px;flex-direction:column;align-items:center}
.letterhead .brand__dot{width:20px;height:20px;margin-bottom:9px}
.letterhead .brand__name{font-size:12px;color:var(--ink)}
.letterhead__sender{position:absolute;left:21px;top:105px;font-size:6px;color:var(--ink);border-bottom:.5px solid var(--ink);padding-bottom:1px}
.letterhead__body{position:absolute;left:23px;top:124px;width:302px;font-size:5px;line-height:1.45;color:var(--body);text-align:justify}
.letterhead__body p{margin-bottom:6px}
.letterhead__body p.gap{margin-top:12px}
.signature{position:absolute;left:220px;top:326px;width:74px;height:50px;background:linear-gradient(120deg,rgba(30,42,56,.05),rgba(30,42,56,.12));border-radius:4px}
.letterhead__footer{position:absolute;left:0;right:0;top:508px;border-top:1px solid #d6d2cc;padding:5px 23px 0;display:flex;gap:60px;font-size:4.3px;line-height:1.45;color:var(--body)}
.letterhead__footer b{font-weight:600;color:var(--ink)}
.contact{display:flex;align-items:center;gap:3px}
.contact i{display:inline-block;width:4px;height:4px;border-radius:50%;background:var(--orange)}

.card{position:absolute;top:43px;height:124px;box-shadow:0 2px 6px rgba(0,0,0,.2)}
.card--front{left:737px;width:192px;background:var(--navy)}
.card--front .brand{right:14px;bottom:22px;flex-direction:row;align-items:center;gap:8px}
.card--front .brand__dot{width:14px;height:14px}
.card--front .brand__name{font-size:13px;color:#fff;letter-spacing:.14em}
.card--back{left:968px;width:194px;background:var(--paper)}
.card--back .brand{left:12px;top:40px}
.card--back .brand__dot{width:16px;height:16px;margin-bottom:8px}
.card--back .brand__name{font-size:8.5px;color:var(--ink)}
.card__person{position:absolute;left:116px;top:30px;font-size:5px;color:var(--ink);line-height:1.5}
.card__person .name{font-size:8.5px;font-weight:600;line-height:1.1}
.card__person .role{font-size:6.5px;margin-bottom:3px}
.card__person .contact i{width:4px;height:4px}

.envelope{position:absolute;left:730px;top:187px;width:434px;height:398px}
.envelope__front{position:absolute;left:0;top:0;width:434px;height:190px;background:var(--paper);box-shadow:0 2px 8px rgba(0,0,0,.18)}
.envelope__window{position:absolute;left:26px;top:93px;width:173px;height:64px;border-radius:9px;background:#fff;border:1px solid #ececec}
.envelope__front .brand{right:24px;top:100px}
.envelope__front .brand__dot{width:22px;height:22px;margin-bottom:14px}
.envelope__front .brand__name{font-size:12.5px;color:var(--ink)}
.envelope__back{position:absolute;left:0;top:208px;width:434px;height:190px;background:linear-gradient(160deg,#fff,#f1f1f1);box-shadow:0 2px 8px rgba(0,0,0,.18)}
.envelope__flap{position:absolute;left:0;top:0}
.envelope__back .brand__dot{position:absolute;left:208px;top:12px;width:18px;height:18px}
</style>
</head>
<body>
  <div class="band band--light"></div>
  <div class="band band--dark"></div>

  <div class="brand brand--hero brand--top"><span class="brand__dot"></span><span class="brand__name">KESTRIM SL</span></div>
  <div class="brand brand--hero brand--mid"><span class="brand__dot"></span><span class="brand__name">KESTRIM SL</span></div>

  <div class="tile tile--stone"><span class="brand__dot"></span><span class="brand__name">KESTRIM SL</span></div>
  <div class="tile tile--white"><span class="brand__dot"></span><span class="brand__name">KESTRIM SL</span></div>

  <section class="letterhead">
    <div class="brand"><span class="brand__dot"></span><span class="brand__name">KESTRIM SL</span></div>
    <div class="letterhead__sender">Your Company · Your adress 12 · 34567 Your town</div>
    <div class="letterhead__body">
      <p>Lorem ipsum dolor sit amet, consectetur adipiscing elit. Maecenas porttitor augue justo, sit amet egestas sapien luctus ultrices. Donec arcu dolor, tincidunt sit amet mi id, laoreet pretium enim. Sed fermentum, dui vel hendrerit sodales, lectus nibh molestie tortor, id fermentum velit urna a diam. Aenean efficitur turpis eu lorem porttitor, et tincidunt leo aliquam. Fusce vel facilisis massa, euismod ullamcorper neque. Suspendisse sodales at nisl sit eleifend. Aliquam nec varius diam. Donec quis enim dictum, tempus nunc et, auctor quam. Suspendisse potenti. Quisque accumsan egestas metus.</p>
      <p>Phasellus id ante id ipsum cursus luctus. Praesent purus elit, ornare sit amet ultricies ac, dignissim a eros. Phasellus vestibulum odio et ipsum mattis maximus. Vivamus suscipit pulvinar tellus eu congue. Aenean quis dui varius, ullamcorper arcu sit amet, vehicula odio. Nunc dui tellus, blandit lacinia sapien eget, venenatis porttitor ex. Sed molestie viverra elit, sit amet condimentum mi finibus et. Cras vel enim, congue at purus vitae, tempor lacinia dolor.</p>
      <p class="gap">Lorem ipsum dolor sit amet, consectetur adipiscing elit. Maecenas porttitor augue justo, sit amet egestas sapien luctus ultrices. Donec arcu dolor, tincidunt sit amet mi id, laoreet pretium enim. Sed fermentum, dui vel hendrerit sodales, lectus nibh molestie tortor, id fermentum velit urna a diam. Aenean efficitur turpis eu lorem porttitor, et tincidunt leo aliquam. Fusce vel facilisis massa, euismod ullamcorper neque. Suspendisse sodales at nisl sit eleifend. Aliquam nec varius diam. Donec quis enim dictum, tempus nunc et, auctor quam. Suspendisse potenti. Quisque accumsan egestas metus.</p>
      <p>Phasellus id ante id ipsum cursus luctus. Praesent purus elit, ornare sit amet ultricies ac, dignissim a eros. Phasellus vestibulum odio et ipsum mattis maximus. Vivamus suscipit pulvinar tellus eu congue. Aenean quis dui varius, ullamcorper arcu sit amet, vehicula odio. Nunc dui tellus, blandit lacinia sapien eget, venenatis porttitor ex. Sed molestie viverra elit, sit amet condimentum mi finibus et. Cras vel enim, congue at purus vitae, tempor lacinia dolor.</p>
    </div>
    <div class="signature" role="img" aria-label="Handschriftliche Unterschrift"></div>
    <footer class="letterhead__footer">
      <div><b>Your Company</b><br>CEO Your Name<br>Your adress 12<br>34567 Your Town</div>
      <div>
        <div class="contact"><i></i>1234 – 56 78 90 00</div>
        <div class="contact"><i></i>1234 – 56 78 90 00</div>
        <div class="contact"><i></i>yourname@musterweb.de</div>
        <div class="contact"><i></i>www.musterweb.de</div>
      </div>
      <div>Bankverbindung<br>Iban: DE00 1234 5678 9012 3456 78<br>BIC:<br>UST-ID: 000000000000</div>
    </footer>
  </section>

  <div class="card card--front">
    <div class="brand"><span class="brand__dot"></span><span class="brand__name">KESTRIM SL</span></div>
  </div>

  <div class="card card--back">
    <div class="brand"><span class="brand__dot"></span><span class="brand__name">KESTRIM SL</span></div>
    <div class="card__person">
      <div class="name">Your Name</div>
      <div class="role">CEO</div>
      <div class="contact"><i></i>Your Adress 12, 34567</div>
      <div style="padding-left:7px">Your Town</div>
      <div class="contact"><i></i>+00 123 456 789</div>
      <div class="contact"><i></i>+00 123 456 789</div>
      <div class="contact"><i></i>yourname@musterweb.de</div>
      <div class="contact"><i></i>www.musterweb.de</div>
    </div>
  </div>

  <div class="envelope">
    <div class="envelope__front">
      <div class="envelope__window"></div>
      <div class="brand"><span class="brand__dot"></span><span class="brand__name">KESTRIM SL</span></div>
    </div>
    <div class="envelope__back">
      <svg class="envelope__flap" width="434" height="52" viewBox="0 0 434 52">
        <polygon points="0,0 434,0 434,16 250,50 184,50 0,16" fill="var(--navy)"/>
      </svg>
      <span class="brand__dot"></span>
    </div>
  </div>
</body>
</html>
```